Stationery Design + Business Cards

Stationary (letterhead as A4 210x297mm and Letter 8.5"x11", preferably both master page + 2nd pages)

Also need business cards, standard size 50x88mm, can be vertical or horizontal.

You can use a front/back design for the business cards, or front only.

Looking at the uploaded file (dolvek, you already have that), I want it to use the first logo on the list (4 colors).

Alternative, try the grayscale version (second file).

I need the following information on the business card (in no particular order, let me know what you come up with): 

Firstname Lastlame 
Title 

Mobile +1 317-555-0147 

Velmarix, Inc. 
24819 Birchwood Ridge Pass 
Harlow Springs, KS 46195 
Tel. +1 555-555-0182 
Fax +1 555-555-0163 

Web: www.velmarix.com 
Twitter: twitter/Velmarix or @Velmarix 
Facebook: facebook.com/Velmarix 

For letterhead, just the company name, address + phone number & fax number 

If you think the phone/fax or something else should not be on the business cards, or something could be missing, let me know.

```html
<!DOCTYPE html>
<html lang="en">
<head>
<meta charset="utf-8">
<title>Velmarix, Inc. – Letterhead</title>
<link rel="stylesheet" href="https://fonts.googleapis.com/css2?family=Crimson+Text&display=swap">
<style>
  :root {
    --paper: #ffffff;
    --name-ink: #2b2b2b;
    --rule: #6f6f6f;
    --ink: #1a1a1a;
  }
  html, body {
    margin: 0;
    padding: 0;
    overflow: hidden;
    background: var(--paper);
  }
  .letterhead {
    position: relative;
    width: 849px;
    height: 1200px;
    background: var(--paper);
    overflow: hidden;
  }
  .brand-name {
    position: absolute;
    left: 54px;
    top: 74px;
    margin: 0;
    font-family: "Crimson Text", serif;
    font-weight: 400;
    font-size: 40px;
    line-height: 1;
    color: var(--name-ink);
  }
  .rule {
    position: absolute;
    left: 51px;
    width: 746px;
    height: 0;
    border-top: 1px solid var(--rule);
  }
  .rule--header { top: 141px; }
  .rule--footer { top: 1071px; }
  .footer-text {
    position: absolute;
    font-family: "Crimson Text", serif;
    font-style: normal;
    font-size: 16.5px;
    line-height: 22px;
    color: var(--ink);
    margin: 0;
  }
  .company-address {
    left: 51px;
    top: 1082px;
  }
  .company-contact {
    right: 52px;
    top: 1108px;
    text-align: right;
  }
</style>
</head>
<body>
  <main class="letterhead">
    <header>
      <p class="brand-name">Velmarix</p>
    </header>
    <div class="rule rule--header"></div>

    <div class="rule rule--footer"></div>
    <address class="footer-text company-address">
      Velmarix, Inc.<br>
      24819 Birchwood Ridge Pass<br>
      Harlow Springs, KS 46195
    </address>
    <p class="footer-text company-contact">
      Tel. +1 555-555-0182<br>
      Fax +1 555-555-0163
    </p>
  </main>
</body>
</html>
```